Stone Harbor Electric website

I need a website for my electrical service business. We do a variety of electrical services for both commercial and residential clients in the Raleigh/Durham area of NC. I would like it to be done by someone who understands the electrical trade. I want a design that uses the color green in my logo. The design should communicate quality in electrical services for jobs big and small. It should have a button to call and a section to email requesting services. A place to list the time of services we offer as well. mobile friendly. First page should have a section for testimonials. A list of services will be provided. Only clean clear pictures. I will provide some.

```html
<!DOCTYPE html>
<html lang="en">
<head>
<meta charset="utf-8">
<title>Stone Harbor Electric</title>
<link href="https://fonts.googleapis.com/css2?family=Audiowide&family=Lato:wght@400;700&display=swap" rel="stylesheet">
<style>
:root{
  --green:#169a3e;
  --green-bright:#22b14c;
  --ink:#1c1c1c;
  --black:#111111;
  --dark:#1a1a1a;
  --white:#ffffff;
  --muted:#cfcfcf;
}
*{box-sizing:border-box;margin:0;padding:0}
html,body{width:1200px;height:3912px;overflow:hidden;background:var(--white);font-family:'Lato',sans-serif;color:var(--ink)}
.page{position:relative;width:1200px;height:3912px;overflow:hidden}
.abs{position:absolute}
.display{font-family:'Audiowide',sans-serif;text-transform:uppercase;letter-spacing:2px}
.btn{position:absolute;display:flex;align-items:center;justify-content:center;font-family:'Audiowide',sans-serif;text-transform:uppercase;font-size:15px;letter-spacing:1px;color:var(--white);background:var(--green)}
.btn.dark{background:var(--black)}

/* header */
.brand{position:absolute;left:75px;top:36px;color:var(--ink);font-family:'Audiowide',sans-serif;font-size:38px;line-height:40px;letter-spacing:2px}
.brand small{display:block;font-size:24px;letter-spacing:14px;line-height:32px;padding-left:70px}
.brand-mark{position:absolute;left:52px;top:46px;width:14px;height:14px;background:var(--green)}
.header-phone{position:absolute;left:615px;top:56px;font-family:'Audiowide',sans-serif;font-size:25px;display:flex;align-items:center;gap:10px}
.nav{position:absolute;left:0;top:141px;width:1200px;height:66px;background:var(--green);display:flex;padding-left:76px}
.nav a{color:var(--white);text-decoration:none;font-size:15px;display:flex;align-items:center;padding:0 24px;text-transform:uppercase;letter-spacing:.3px}
.nav a.active{background:var(--black);padding:0 27px}
.nav a:nth-child(n+2){margin-left:4px}

/* hero */
.hero-photo{position:absolute;left:0;top:207px;width:1200px;height:636px;background:linear-gradient(100deg,#6b6b6b 0%,#8a8580 40%,#6c6a5e 70%,#a8a857 100%)}
.hero-title{position:absolute;left:0;top:372px;width:1200px;text-align:center;color:var(--white);font-size:72px;line-height:78px}
.hero-sub{position:absolute;left:0;top:534px;width:1200px;text-align:center;color:var(--white);font-size:26px;line-height:34px}
.dots{position:absolute;left:564px;top:744px;display:flex;gap:10px}
.dots span{width:10px;height:10px;border-radius:50%;background:var(--white)}
.dots span:first-child{background:var(--green-bright)}
.schedule-tab{position:absolute;left:365px;top:778px;width:467px;height:65px}
.schedule-tab b{position:absolute;left:0;top:0;width:467px;line-height:72px;text-align:center;color:var(--white);font-weight:400;font-size:25px}

/* form */
.form-band{position:absolute;left:0;top:843px;width:1200px;height:134px;background:var(--dark)}
.field{position:absolute;top:889px;height:47px;background:var(--white);font-size:14px;color:#333;padding-left:13px;display:flex;align-items:center}

/* services */
.service-bg{position:absolute;left:0;top:977px}
.section-title{position:absolute;left:0;width:1200px;text-align:center;color:var(--white);font-size:38px}
.card{position:absolute;width:331px;height:266px;box-shadow:0 2px 6px rgba(0,0,0,.3)}
.card .label{position:absolute;left:0;top:108px;width:100%;height:48px;background:rgba(20,20,20,.85);color:var(--white);display:flex;align-items:center;justify-content:center;font-size:17px;letter-spacing:1.5px}

/* welcome */
.welcome-band{position:absolute;left:0;top:1782px;width:1200px;height:501px;background:var(--dark)}
.welcome-title{position:absolute;left:75px;top:1836px;color:var(--white);font-size:36px;line-height:44px}
.welcome-text{position:absolute;left:75px;top:1990px;width:470px;color:var(--white);font-size:16px;line-height:30.5px}

/* cta */
.cta{position:absolute;left:164px;top:2373px;width:872px;height:221px;background:var(--green)}
.cta h2{position:absolute;top:46px;width:100%;text-align:center;color:var(--white);font-weight:400;font-size:34px}
.cta p{position:absolute;top:95px;width:100%;text-align:center;color:var(--white);font-size:20px}

/* testimonials */
.testi-title{position:absolute;left:709px;top:2778px;color:var(--white);font-size:40px}
.testi-name{position:absolute;left:709px;top:2855px;color:var(--green-bright);font-size:18px}
.testi-text{position:absolute;left:709px;top:2884px;width:430px;color:var(--white);font-size:14.5px;line-height:30px}

/* subscribe */
.sub-band{position:absolute;left:0;top:3433px;width:1200px;height:479px;background:var(--dark)}
.subscribe{position:absolute;left:137px;top:3273px;width:926px;height:259px;background:var(--green)}
.subscribe h2{position:absolute;top:42px;width:100%;text-align:center;color:var(--white);font-weight:400;font-size:38px}
.subscribe p{position:absolute;top:99px;width:100%;text-align:center;color:var(--white);font-size:14px}
.sub-input{position:absolute;left:117px;top:145px;width:546px;height:60px;background:#f2f2f2;display:flex;align-items:center;padding-left:22px;gap:16px;font-size:14px;color:#333}
.sub-btn{position:absolute;left:663px;top:145px;width:145px;height:60px;background:var(--black);color:var(--white);display:flex;align-items:center;justify-content:center;font-size:17px}

/* footer */
.f-head{position:absolute;top:3586px;color:var(--white);font-size:16px;letter-spacing:1.5px}
.f-list{position:absolute;top:3628px;color:var(--muted);font-size:14px;line-height:31px;list-style:none}
.f-list .hl{color:var(--green-bright);font-weight:700}
.socials{position:absolute;left:887px;top:3630px;display:flex;gap:22px}
.socials span{width:22px;height:22px;border-radius:50%;background:var(--white)}
.f-brand{position:absolute;left:884px;top:3704px;width:207px;text-align:center;color:var(--white);font-family:'Audiowide',sans-serif;font-size:22px;line-height:24px;letter-spacing:1px}
.f-brand small{display:block;font-size:13px;letter-spacing:7px;line-height:18px}
.copyright{position:absolute;left:0;top:3826px;width:1200px;height:86px;border-top:1px solid #333;color:var(--muted);font-size:13px;display:flex;align-items:center;justify-content:center}
</style>
</head>
<body>
<div class="page">

  <!-- header -->
  <div class="brand-mark"></div>
  <div class="brand">STONE HARBOR<small>ELECTRIC</small></div>
  <div class="header-phone">
    <svg width="22" height="22" viewBox="0 0 24 24"><path fill="#1c1c1c" d="M6.6 10.8c1.4 2.8 3.8 5.1 6.6 6.6l2.2-2.2c.3-.3.7-.4 1-.2 1.1.4 2.3.6 3.6.6.6 0 1 .4 1 1V20c0 .6-.4 1-1 1C10.6 21 3 13.4 3 4c0-.6.4-1 1-1h3.5c.6 0 1 .4 1 1 0 1.3.2 2.5.6 3.6.1.3 0 .7-.2 1z"/></svg>
    1-800-555-0142
  </div>
  <div class="btn" style="left:948px;top:47px;width:178px;height:46px;font-size:17px">Contact Us</div>

  <nav class="nav">
    <a class="active">Home</a><a>About Us</a><a>Services</a><a>Commercial</a><a>Residential</a><a>Testimonials</a><a>Blog</a><a>Contact Us</a>
  </nav>

  <!-- hero -->
  <div class="hero-photo" role="img" aria-label="Electrician in safety glasses and hi-vis vest testing wiring in an electrical panel"></div>
  <div class="hero-title display">Stone Harbor<br>Electric</div>
  <div class="hero-sub">Vestibulum ante ipsum primis in faucibus orci luctus<br>et ultrices posuere..</div>
  <div class="btn" style="left:520px;top:623px;width:162px;height:45px">Read More</div>
  <div class="dots"><span></span><span></span><span></span><span></span></div>
  <div class="schedule-tab">
    <svg width="467" height="65" class="abs" style="left:0;top:0"><polygon points="18,0 449,0 467,65 0,65" fill="#169a3e"/></svg>
    <b class="display">Schedule a Services</b>
  </div>

  <!-- form -->
  <div class="form-band"></div>
  <div class="field" style="left:75px;width:176px">Name</div>
  <div class="field" style="left:258px;width:176px">Email Address</div>
  <div class="field" style="left:442px;width:176px">Phone No</div>
  <div class="field" style="left:627px;width:175px">Date
    <svg class="abs" style="right:12px;top:16px" width="14" height="15" viewBox="0 0 14 15"><rect x="1" y="2" width="12" height="12" fill="none" stroke="#333" stroke-width="1.5"/><rect x="1" y="2" width="12" height="3" fill="#333"/><rect x="3" y="7" width="2" height="2" fill="#333"/><rect x="6" y="7" width="2" height="2" fill="#333"/><rect x="9" y="7" width="2" height="2" fill="#333"/><rect x="3" y="10" width="2" height="2" fill="#333"/><rect x="6" y="10" width="2" height="2" fill="#333"/></svg>
  </div>
  <div class="field" style="left:811px;width:176px">Enter About Project</div>
  <div class="btn" style="left:998px;top:889px;width:128px;height:47px;font-size:16px">Submit</div>

  <!-- services -->
  <svg class="service-bg" width="1200" height="755"><polygon points="0,0 1200,0 0,755" fill="#169a3e"/></svg>
  <h2 class="section-title display" style="top:1030px;font-weight:400">Service Offers</h2>

  <div class="card" style="left:75px;top:1109px;background:linear-gradient(135deg,#8a8a88,#5a4a3e 60%,#3a3a3a)" role="img" aria-label="Electrician repairing wiring with a screwdriver"><div class="label display">General Repairs</div></div>
  <div class="card" style="left:434px;top:1109px;background:linear-gradient(135deg,#5a4034,#b8743e 55%,#2e2622)" role="img" aria-label="Electrician installing a light bulb fixture"><div class="label display">Lighting Upgrades</div></div>
  <div class="card" style="left:796px;top:1109px;background:linear-gradient(135deg,#e6e6e6,#c65a2c 55%,#2e3542)" role="img" aria-label="Worker in orange gear installing panel wiring"><div class="label display">New Installation</div></div>

  <div class="card" style="left:75px;top:1417px;background:linear-gradient(135deg,#d8dde3,#e07a2a 50%,#2c3e8a)" role="img" aria-label="Multimeter testing a switch panel"><div class="label display">Transfer Switches</div></div>
  <div class="card" style="left:434px;top:1417px;background:linear-gradient(135deg,#f1f1f1,#dcdcdc 55%,#c8b8a8)" role="img" aria-label="Electrician on a ladder fitting a ceiling fan"><div class="label display">Ceiling Fans</div></div>
  <div class="card" style="left:796px;top:1417px;background:linear-gradient(135deg,#bfc3c7,#6a6e73 50%,#2f58a8)" role="img" aria-label="Electrician with clipboard beside circuit cabinets"><div class="label display">Circuit Replacements</div></div>

  <!-- welcome -->
  <div class="welcome-band"></div>
  <svg class="abs" style="left:560px;top:1759px" width="640" height="547">
    <polygon points="0,89 18,89 84,547 66,547" fill="#169a3e"/>
  </svg>
  <div class="abs" style="left:574px;top:1759px;width:626px;height:547px;clip-path:polygon(0 0,100% 0,100% 100%,68px 100%);background:linear-gradient(110deg,#7a7a74,#5a4a3e 45%,#3a4030 75%,#6a7060)" role="img" aria-label="Electrician working on an outdoor service panel"></div>
  <h2 class="welcome-title display" style="font-weight:400">Welcome to<br>Stone Harbor<br>Electric</h2>
  <p class="welcome-text">Sed ut perspiciatis unde omnis iste natus error sit voluptatem accusantium doloremque laudantium, totam rem aperiam, eaque ipsa quae ab illo inventore veritatis et quasi architecto beatae vitae dicta sunt explicabo. Nemo enim ipsam voluptatem quia voluptas.</p>
  <div class="btn" style="left:76px;top:2171px;width:162px;height:47px">Read More</div>

  <!-- cta -->
  <div class="cta">
    <h2 class="display">What can we do for you?</h2>
    <p>Sed ut perspiciatis unde omnis iste natus error sit&nbsp; voluptatem.</p>
  </div>
  <div class="btn dark" style="left:519px;top:2506px;width:163px;height:46px">Book Now</div>

  <!-- testimonials -->
  <div class="abs" style="left:560px;top:2681px;width:640px;height:503px;background:linear-gradient(120deg,#2a2a28,#3a3a36 50%,#2a2824)" role="img" aria-label="Dark close-up of electrical wiring"></div>
  <div class="abs" style="left:0;top:2658px;width:624px;height:547px;clip-path:polygon(0 0,100% 0,63px 0,100% 0,60px 100%,0 100%);"></div>
  <div class="abs" style="left:0;top:2658px;width:624px;height:547px;clip-path:polygon(0 0,100% 0,92% 100%,0 100%);background:linear-gradient(100deg,#6a6056,#8a8a86 30%,#3a6ac8 60%,#9ab8e8 85%)" role="img" aria-label="Electrician reviewing plans beside an open blue-lit panel"></div>
  <div class="abs" style="left:498px;top:2842px;width:174px;height:174px;border-radius:50%;border:4px solid var(--white);background:linear-gradient(160deg,#e8e8e8,#c9a48a)" role="img" aria-label="Customer portrait"></div>
  <h2 class="testi-title display" style="font-weight:400">Testimonials</h2>
  <div class="testi-name display">Name Heading</div>
  <p class="testi-text">“&nbsp; Vestibulum ante ipsum primis in faucibus orci luctus et ultrices posuere cubilia lobortis turpis in odio blandit aliquam nibh sed quia consequuntur magni dolores eos qui ratione voluptatem sequ..”</p>
  <svg class="abs" style="left:712px;top:3036px" width="90" height="34"><polyline points="20,2 6,17 20,32" fill="none" stroke="#6a6a6a" stroke-width="2"/><polyline points="70,2 84,17 70,32" fill="none" stroke="#6a6a6a" stroke-width="2"/></svg>

  <!-- subscribe -->
  <div class="sub-band"></div>
  <div class="subscribe">
    <h2 class="display">Email Subscribe</h2>
    <p>Vestibulum ante ipsum primis in faucibus orci luctus et ultrices posuere cubilia lobortis turpis in odio blandit aliquam nibh</p>
    <div class="sub-input">
      <svg width="15" height="12" viewBox="0 0 15 12"><rect width="15" height="12" fill="#444"/><polyline points="0,0 7.5,6 15,0" fill="none" stroke="#f2f2f2" stroke-width="1.5"/></svg>
      Enter Email Address
    </div>
    <div class="sub-btn display">Sign Up</div>
  </div>

  <!-- footer -->
  <div class="f-head display" style="left:75px">Site Map</div>
  <ul class="f-list" style="left:75px"><li>Home</li><li>About Us</li><li>Services</li><li>Commercial</li><li>Residential</li></ul>
  <ul class="f-list" style="left:217px"><li>Testimonials</li><li>Blog</li><li>Contact Us</li></ul>

  <div class="f-head display" style="left:368px">Services</div>
  <ul class="f-list" style="left:368px"><li>Sed ut perspiciatis</li><li>Unde omnis iste</li><li>Natus error sit voluptatem</li><li>Accusantium</li><li>Nemo enim ipsam</li></ul>

  <div class="f-head display" style="left:614px">Contact Info</div>
  <ul class="f-list" style="left:614px;line-height:25px">
    <li class="hl">Stone Harbor Electric</li>
    <li style="margin-top:6px">418 Harbor Ridge Rd #12,</li>
    <li>Cary, NC 27511</li>
    <li style="margin-top:6px;display:flex;align-items:center;gap:18px"><svg width="12" height="12" viewBox="0 0 24 24"><path fill="#cfcfcf" d="M6.6 10.8c1.4 2.8 3.8 5.1 6.6 6.6l2.2-2.2c.3-.3.7-.4 1-.2 1.1.4 2.3.6 3.6.6.6 0 1 .4 1 1V20c0 .6-.4 1-1 1C10.6 21 3 13.4 3 4c0-.6.4-1 1-1h3.5c.6 0 1 .4 1 1 0 1.3.2 2.5.6 3.6.1.3 0 .7-.2 1z"/></svg>1-800-555-0142</li>
    <li style="margin-top:4px;display:flex;align-items:center;gap:18px"><svg width="12" height="10" viewBox="0 0 15 12"><rect width="15" height="12" fill="#cfcfcf"/><polyline points="0,0 7.5,6 15,0" fill="none" stroke="#1a1a1a" stroke-width="1.5"/></svg>hello@stoneharborelectric.com</li>
  </ul>

  <div class="f-head display" style="left:887px">Follow Us</div>
  <div class="socials"><span></span><span></span><span></span><span></span><span></span></div>
  <div class="f-brand">STONE HARBOR<small>ELECTRIC</small></div>

  <div class="copyright">Copyright © 2021 Company Name All Right Reserved</div>
</div>
</body>
</html>
```